Business Card Design

Harbor Refuse 342 is a waste collection business contracted to remove waste from city streets, parks and caravan parks.

Target Market(s)

CEO and Managing Directors

Industry/Entity Type

Business

Contact Information for Business Card

Harbor Refuse 342
Manager
Dale Pickett
0439516204
harborrefuse342@quillmail.com.au

Colors
33a6d7
ecf7fb

Requirements
Must have
• Must have eye catching design that stands out above others ( tender process can be very competitive ).
Nice to have
• A garbage truck on or in the logo somehow

```html
<!DOCTYPE html>
<html lang="en">
<head>
<meta charset="utf-8">
<title>Harbor Refuse 342 – Business Card</title>
<link rel="stylesheet" href="https://fonts.googleapis.com/css2?family=Bebas+Neue&family=Mr+Dafoe&family=Jost:wght@500;600&display=swap">
<style>
  :root {
    --card-bg: #ecf7fb;
    --brand-blue: #33a6d7;
    --ink: #231f20;
  }
  * { margin: 0; padding: 0; box-sizing: border-box; }
  html, body {
    width: 1200px;
    height: 741px;
    overflow: hidden;
    background: var(--card-bg);
  }
  .card {
    position: relative;
    width: 1200px;
    height: 741px;
    background: var(--card-bg);
    color: var(--ink);
  }
  .side-ornament {
    position: absolute;
    top: 45px;
    width: 30px;
    height: 650px;
    border-radius: 15px;
    background: linear-gradient(180deg, rgba(51,166,215,0.35), rgba(51,166,215,0.75) 50%, rgba(51,166,215,0.35));
  }
  .side-ornament--left { left: 46px; }
  .side-ornament--right { left: 1124px; }
  .company-name {
    position: absolute;
    top: 62px;
    left: 0;
    width: 1200px;
    text-align: center;
    font-family: "Bebas Neue", "Arial Narrow", sans-serif;
    font-weight: 400;
    font-size: 124px;
    line-height: 1;
    letter-spacing: 1px;
    color: var(--ink);
  }
  .divider {
    position: absolute;
    left: 380px;
    width: 440px;
    height: 28px;
  }
  .divider--top { top: 237px; }
  .divider--bottom { top: 481px; }
  .holder-name {
    position: absolute;
    top: 272px;
    left: 0;
    width: 1200px;
    text-align: center;
    font-family: "Mr Dafoe", cursive;
    font-size: 150px;
    line-height: 1;
    color: var(--ink);
  }
  .job-title {
    position: absolute;
    top: 535px;
    left: 0;
    width: 1200px;
    text-align: center;
    font-family: "Jost", "Futura", sans-serif;
    font-weight: 600;
    font-size: 54px;
    line-height: 1;
  }
  .phone {
    position: absolute;
    top: 590px;
    left: 0;
    width: 1200px;
    text-align: center;
    font-family: "Jost", "Futura", sans-serif;
    font-weight: 600;
    font-size: 64px;
    line-height: 1;
    letter-spacing: 1px;
  }
  .email {
    position: absolute;
    top: 666px;
    left: 0;
    width: 1200px;
    text-align: center;
    font-family: "Jost", "Futura", sans-serif;
    font-weight: 500;
    font-size: 32px;
    line-height: 1;
    color: var(--brand-blue);
  }
</style>
</head>
<body>
<main class="card">
  <div class="side-ornament side-ornament--left" role="img" aria-label="Vertical twisted-line border ornament"></div>
  <div class="side-ornament side-ornament--right" role="img" aria-label="Vertical twisted-line border ornament"></div>

  <h1 class="company-name">HARBOR REFUSE 342</h1>

  <svg class="divider divider--top" viewBox="0 0 440 28" aria-hidden="true">
    <line x1="6" y1="14" x2="186" y2="14" stroke="#33a6d7" stroke-width="3"/>
    <line x1="254" y1="14" x2="434" y2="14" stroke="#33a6d7" stroke-width="3"/>
    <rect x="209" y="3" width="22" height="22" transform="rotate(45 220 14)" fill="#231f20"/>
  </svg>

  <p class="holder-name">Dale Pickett</p>

  <svg class="divider divider--bottom" viewBox="0 0 440 28" aria-hidden="true">
    <line x1="6" y1="14" x2="186" y2="14" stroke="#33a6d7" stroke-width="3"/>
    <line x1="254" y1="14" x2="434" y2="14" stroke="#33a6d7" stroke-width="3"/>
    <rect x="209" y="3" width="22" height="22" transform="rotate(45 220 14)" fill="#231f20"/>
  </svg>

  <p class="job-title">Manager</p>
  <p class="phone">0439516204</p>
  <p class="email">harborrefuse342@quillmail.com.au</p>
</main>
</body>
</html>
```